Preisliste für Tochterunternehmen im Baustoff-Sektor
Zielgruppe
Wir möchten für unserer Tochterunternehmen im Baustoff-Sektor eine gestaltete Preisliste.
Es gibt eine Liste für Privat- und Geschäftskunden die bisher mit MS-Office einfach gehalten war.
Aufgabenstellung
Logo und der aktuelle Briefkopf sind in der Anlage. Das Design sollte zum CI passen (siehe Briefkopf)
Vom Platzbedarf her sollte sich an der alten Liste orientiert werden. Weitere Infos und Bilder gibt es unter www.tannhoferwerk.de
Genaue Firmenbezeichnung usw. finden Sie in der Preisliste auf der letzten Seite

```html
<!DOCTYPE html>
<html lang="de">
<head>
<meta charset="utf-8">
<title>Preisliste – Tannhofer Werk</title>
<link href="https://fonts.googleapis.com/css2?family=Source+Sans+3:ital,wght@0,400;0,600;0,700;0,900;1,400&display=swap" rel="stylesheet">
<style>
:root{
  --backdrop:#e3e0db;
  --paper:#f4f4f5;
  --ink:#2b2724;
  --brand:#6a6155;
  --brand-soft:#a39a8e;
  --cell-light:#dddbd9;
  --cell-dark:#c3bfba;
  --band-dark:#8c857d;
  --band-light:#aaa49d;
}
*{box-sizing:border-box;margin:0;padding:0}
html,body{width:1200px;height:1012px;overflow:hidden}
body{background:var(--backdrop);font-family:"Source Sans 3",sans-serif;color:var(--ink);position:relative}
.sheet{position:absolute;top:106px;width:560px;height:800px;background:var(--paper);box-shadow:0 1px 3px rgba(0,0,0,.08)}
.sheet--front{left:30px}
.sheet--back{left:610px}
.sheet__band{position:absolute;left:0;right:0;bottom:0;height:8px;display:flex}
.sheet__band span:first-child{width:50%;background:var(--band-light)}
.sheet__band span:last-child{flex:1;background:var(--band-dark);margin-left:2px}

.brand{position:absolute;top:46px;right:52px;display:flex;align-items:center;gap:8px;font-weight:900;font-size:22px;line-height:1;color:var(--brand);letter-spacing:-.3px;text-transform:uppercase}
.brand__mark{width:18px;height:18px;background:var(--brand-soft)}

.title{position:absolute;left:58px;top:144px}
.title__main{display:flex;align-items:flex-end;gap:5px}
.title__word{font-weight:700;font-size:21px;letter-spacing:1.4px;color:var(--brand);line-height:1}
.title__sub{font-size:7.6px;line-height:8px;color:var(--brand-soft);padding-bottom:3px}
.title__date{font-size:8.4px;margin-top:4px}

.contact{position:absolute;left:371px;top:124px;border-left:1px solid var(--ink);padding-left:8px;font-size:8.4px;line-height:13.5px}
.contact__line{display:flex;align-items:center;gap:5px}
.contact__line svg{width:9px;height:9px;stroke:#777;fill:none;stroke-width:1.2}

.section{position:absolute;left:59px;width:433px}
.section--flow{position:static;width:433px}
.section__head{display:grid;grid-template-columns:1fr 68px 68px;align-items:end;margin-bottom:4px}
.section__head h2{font-size:10.4px;font-weight:700}
.section__head span{font-size:8px;text-align:center;white-space:nowrap}

.group{margin-bottom:4px}
.row{display:grid;grid-template-columns:1fr 68px 68px;gap:2px;margin-bottom:1px;font-size:8.3px;line-height:10.8px}
.row > div{padding:1.6px 4px;background:var(--cell-light)}
.row--dark > div{background:var(--cell-dark)}
.row .price{text-align:right;padding-right:8px;display:flex;flex-direction:column;justify-content:flex-end;align-items:flex-end}
.row b{font-weight:700}
.row .tier{float:right;text-align:right;padding-right:24px}

.note{font-size:6.2px;font-style:italic;margin-top:4px}

.back-body{position:absolute;left:59px;top:38px;width:433px}
.back-body .section--flow + .section--flow{margin-top:10px}
.terms{font-size:6.3px;line-height:8px;text-align:justify;margin-top:6px}
</style>
</head>
<body>

<article class="sheet sheet--front">
  <div class="brand"><span>Tannhofer Werk</span><span class="brand__mark"></span></div>

  <header class="title">
    <div class="title__main">
      <span class="title__word">PREISLISTE</span>
      <span class="title__sub">für Tannhofer Grauwacke aus<br>unserem Werk Tannhof</span>
    </div>
    <p class="title__date">gültig ab dem 01.03.2018</p>
  </header>

  <address class="contact" style="font-style:normal">
    <div>Lindenweg 12</div>
    <div>56999 Tannhof</div>
    <div class="contact__line"><svg viewBox="0 0 10 10"><path d="M2 1l2 2-1 1.5c.6 1.2 1.4 2 2.5 2.5L7 6l2 2-1.5 1.5C4.5 9 1 5.5.5 2.5z"/></svg>01234 - 56 -0</div>
    <div class="contact__line"><svg viewBox="0 0 10 10"><rect x="1" y="4" width="8" height="4"/><rect x="2.5" y="1" width="5" height="3"/><rect x="2.5" y="7" width="5" height="2.5"/></svg>01234 - 56 -50</div>
    <div class="contact__line"><svg viewBox="0 0 10 10"><rect x=".8" y="2" width="8.4" height="6"/><path d="M.8 2L5 5.5 9.2 2"/></svg>info@tannhoferwerk.de</div>
    <div class="contact__line"><svg viewBox="0 0 10 10"><rect x=".8" y="1.5" width="8.4" height="7"/><path d="M.8 3.5h8.4"/></svg>www.tannhoferwerk.de</div>
  </address>

  <section class="section" style="top:239px">
    <div class="section__head"><h2>Schüttgüter</h2><span>Netto ab Werk</span><span>Brutto ab Werk</span></div>
    <div class="group">
      <div class="row"><div>Vorsiebmaterial*</div><div class="price">5,00 €/t</div><div class="price">5,95 €/t</div></div>
      <div class="row row--dark"><div>Mineralgemisch 0/32 ; 0/45*</div><div class="price">7,50 €/t</div><div class="price">8,93 €/t</div></div>
      <div class="row"><div>Steinmaterial gebrochen 0/100 ; 0/150 ; 0/200*</div><div class="price">6,50 €/t</div><div class="price">7,74 €/t</div></div>
    </div>
    <div class="group">
      <div class="row row--dark"><div>Frostschutz-Splitt 0/32 ; 0/45</div><div class="price">9,00 €/t</div><div class="price">10,71 €/t</div></div>
      <div class="row"><div>Schottertragschicht 0/32 ; 0/45</div><div class="price">10,00 €/t</div><div class="price">11,90 €/t</div></div>
    </div>
    <div class="group"><div class="row row--dark"><div>Brechsand 0/3; 0/4*</div><div class="price">8,00 €/t</div><div class="price">9,52 €/t</div></div></div>
    <div class="group"><div class="row"><div>Splitt 2/5; 2/8; 5/8; 8/16; 16/22; 16/32; 22/32; 32/56</div><div class="price">16,00 €/t</div><div class="price">19,04 €/t</div></div></div>
    <div class="group"><div class="row row--dark"><div>Splitt gewaschen 2/4; 4/8; 8/16; 16/22</div><div class="price">18,00 €/t</div><div class="price">21,42 €/t</div></div></div>
    <div class="group"><div class="row"><div>Splitt-Gemische 0/5 ; 0/8 ; 0/11 ; 0/16*</div><div class="price">13,00 €/t</div><div class="price">15,47 €/t</div></div></div>
    <div class="group">
      <div class="row row--dark"><div>Wingertsschotter 20/60*</div><div class="price">15,00 €/t</div><div class="price">17,85 €/t</div></div>
      <div class="row"><div>Schotter 40/80 ; 56/90*</div><div class="price">14,00 €/t</div><div class="price">16,66 €/t</div></div>
      <div class="row row--dark"><div>Schotter 70/100 ; 70/150* als Gabionen Füllmaterial</div><div class="price">20,00 €/t</div><div class="price">23,80 €/t</div></div>
    </div>
    <div class="group"><div class="row"><div>Sackware 2/5; 8/16 (20 kg)</div><div class="price">5,00 €/St</div><div class="price">5,95 €/St</div></div></div>
    <p class="note">* nicht güteüberwacht &nbsp;|&nbsp; Schüttgüter-Kleinmengen bis 3 to werden pauschal mit 3 to abgerechnet</p>
  </section>

  <section class="section" style="top:543px">
    <div class="section__head"><h2>Handsortierte- und bearbeitete Materialien</h2><span>Netto ab Werk</span><span>Brutto ab Werk</span></div>
    <div class="group"><div class="row"><div>Mauersteine für <b>Trockenmauerwerk</b>, nach DIN 1053 Bild 14<br>Schichthöhe ca. 10-35 cm, Einbindetiefe ca. 15-40 cm,<br><b>unbearbeitet</b>, von Hand sortiert, Gewicht ca. 2-70 kg/Stein<br>Ergiebigkeit ca. 1,2-1,5 m²/t</div><div class="price">115,00 €/t</div><div class="price">136,85 €/t</div></div></div>
    <div class="group"><div class="row row--dark"><div>Wie vor, jedoch Einbindetiefe ca. 10-30 cm, Schichthöhe von ca. 10-35 cm<br>Ergiebigkeit ca. 1,8-2,0 m²/t</div><div class="price">125,00 €/t</div><div class="price">148,75 €/t</div></div></div>
    <div class="group"><div class="row"><div>Mauersteine für <b>Bruchsteinmauerwerk</b> nach DIN 1053 Bild 16<br>Schichthöhe ca. 10-35 cm, Einbindetiefe ca. 10-30 cm,<br><b>unbearbeitet</b>, von Hand sortiert, Gewicht ca. 2-50 kg/Stein<br>Ergiebigkeit ca. 2,0-2,4 m²/t</div><div class="price">125,00 €/t</div><div class="price">148,75 €/t</div></div></div>
    <div class="group"><div class="row row--dark"><div>Wie vor, jedoch Einbindetiefe &lt; 15 cm, Schichthöhe von 8-25 cm<br>Ergiebigkeit ca. 3,5-4,0 m²/t</div><div class="price">240,00 €/t</div><div class="price">285,60 €/t</div></div></div>
  </section>

  <div class="sheet__band"><span></span><span></span></div>
</article>

<article class="sheet sheet--back">
  <div class="back-body">
    <section class="section--flow">
      <div class="section__head"><h2>Handsortierte- und bearbeitete Materialien</h2><span>Netto ab Werk</span><span>Brutto ab Werk</span></div>
      <div class="group"><div class="row"><div><b>Schichtsteine</b>, von Hand sortiert und masch. bearbeitet nach DIN 1053 Bild 17<br>Sichtfläche <b>spaltrauh</b>, Schichthöhe von 8-25 cm, Einbautiefe ca. 12-25 cm<br>Ergiebigkeit ca. 2,6-3,0 m²/t</div><div class="price">255,00 €/t</div><div class="price">303,45 €/t</div></div></div>
      <div class="group"><div class="row row--dark"><div>wie vor, jeoch Einbindetiefe &lt; 15 cm, Schichthöhe von 4-15 cm<br>Ergiebigkeit ca. 4,0-4,5 m²/t</div><div class="price">310,00 €/t</div><div class="price">368,90 €/t</div></div></div>
      <div class="group"><div class="row"><div><b>Schichtsteine</b>, von Hand bearbeitet und behauen nach DIN 1053 Bild 17<br>Sichtfläche <b>bossiert</b>, Schichthöhe 4-12 ; 12-25 und 4-25 cm<br>Einbindetiefe ca. 8-25 cm</div><div class="price">150,00 €/t</div><div class="price">178,50 €/t</div></div></div>
      <div class="group"><div class="row row--dark"><div><b>Kräuterschnecke</b>, 1x Holzkiste mit handsortierten Mauersteinen,<br>1 Big Bag mit 500 kg Splitt 0/16, Aufbauanleitung</div><div class="price">350,00 €/t</div><div class="price">416,50 €/t</div></div></div>
      <div class="group"><div class="row"><div><b>Böschungspflaster</b> ca. 25-30 cm stark, unbearbeitet,<br>von Hand sortiert, Gewicht ca. 30-100 kg/Stein<br>Ergiebigkeit ca. 1,5 - 2,0 m²/t</div><div class="price">90,00 €/t</div><div class="price">107,10 €/t</div></div></div>
      <div class="group"><div class="row row--dark"><div><b>Findlingsmauersteine</b>, Kantenlänge ca. 30-60 / 60-100 / 100-140 cm,<br>lagerhaft</div><div class="price">120,00 €/t</div><div class="price">142,80 €/t</div></div></div>
      <div class="group"><div class="row"><div><b>Findlingssteine</b>, polygonal / unregelmäßig</div><div class="price">90,00 €/t</div><div class="price">107,10 €/t</div></div></div>
      <div class="group"><div class="row row--dark"><div><span class="tier">&lt; 1 t<br>&gt; 1 t</span><b>Findling Einzelstück</b>, eckig oder rund<br>&nbsp;</div><div class="price" style="justify-content:flex-start">160,00 €/t<br>240,00 €/t</div><div class="price" style="justify-content:flex-start">190,40 €/t<br>285,60 €/t</div></div></div>
      <div class="group"><div class="row"><div><b>Rollschicht</b>, von Hand bearbeitet (Höhe/Breite)<br>150/300 ; 100/400<br>150/400 ; 200/450<br>200/500 ; 250/500<br>200/550 ; 250/550</div><div class="price">145,00 €/t<br>145,00 €/t<br>155,00 €/t<br>165,00 €/t</div><div class="price">172,55 €/t<br>172,55 €/t<br>184,45 €/t<br>196,35 €/t</div></div></div>
      <div class="group"><div class="row row--dark"><div><b>Bogensteine</b>, von Hand bearbeitet, bis 20 cm hoch</div><div class="price">120,00 €/t</div><div class="price">142,80 €/t</div></div></div>
      <div class="group"><div class="row"><div><b>Ecksteine</b>, von Hand bearbeitet</div><div class="price">95,00 €/t</div><div class="price">113,05 €/t</div></div></div>
      <div class="group"><div class="row row--dark"><div><b>Platten</b>, unregelmäßig, unbearbeitet, 1-3 cm stark</div><div class="price">45,00 €/t</div><div class="price">53,55 €/t</div></div></div>
      <div class="group"><div class="row"><div><b>Platten</b> wie vor, jedoch 4-7 cm stark</div><div class="price">50,00 €/t</div><div class="price">59,50 €/t</div></div></div>
      <div class="group"><div class="row row--dark"><div><b>Mauerabdeckplatten</b>, einseitig bearb. ansonsten unregelmäßig, 4-7 cm stark</div><div class="price">55,00 €/t</div><div class="price">59,50 €/t</div></div></div>
    </section>

    <section class="section--flow">
      <div class="section__head"><h2>Zubehör</h2><span>Netto ab Werk</span><span>Brutto ab Werk</span></div>
      <div class="group"><div class="row"><div>Grauwacke-<b>Riemchen</b>, Einbindetiefe 2 cm, Schichthöhe 4-19 cm</div><div class="price">160,00 €/t</div><div class="price">190,40 €/t</div></div></div>
      <div class="group"><div class="row row--dark"><div>Basaltlava-<b>Abdeckplatten</b>, bis 4 cm stark</div><div class="price">220,00 €/t</div><div class="price">261,80 €/t</div></div></div>
    </section>

    <section class="section--flow">
      <div class="section__head"><h2>Logistik und Verpackung</h2><span>Netto ab Werk</span><span>Brutto ab Werk</span></div>
      <div class="group"><div class="row"><div>Schüttgüter in <b>Big-Bags</b> (keine Gutschrift bei Rückgabe)</div><div class="price">30,00 €/t</div><div class="price">35,70 €/t</div></div></div>
      <div class="group"><div class="row row--dark"><div>Wertsteine in <b>Holz-Einweg-Kisten</b> (keine Gutschrift bei Rückgabe)</div><div class="price">40,00 €/t</div><div class="price">47,60 €/t</div></div></div>
      <div class="group"><div class="row"><div>Verladung von Rollschicht, Ecksteinen u. Bogensteinen<br>in <b>Stahl-Mehrwegplatten</b> (Rückgabepflicht)<br>Gutschrift bei frachtfreier Rückgabe</div><div class="price">50,00 €/t<br>45,00 €/t</div><div class="price">59,50 €/t<br>53,55 €/t</div></div></div>
    </section>

    <p class="terms">Die Preise verstehen sich ab Werk frei verladen, zuzüglich der gesetzlichen Mehrwertsteuer. Schüttgüter in größeren Mengen können aus laufender Produkton und aus Lagervorrat ständig geliefert werden. Für Lieferungen frei Baustelle mit Lastzügen oder Solofahrzeugen steht genügend Frachtraum zur Verfügung. Preise erhalten Sie auf Anfrage. Von Hand sortiert und bearbeitete Materialien bitten wir rechtzeitig zu bestellen. Durch den sehr hohen Lohnkostenanteil der Materialien ist der Verkauf nur gegen Barzahlung bei Abholung möglich. Sonderanfertigungen in Rollschicht, Bogensteinen, Ecksteinen usw. sind möglich.</p>
  </div>

  <div class="sheet__band"><span></span><span></span></div>
</article>

</body>
</html>
```